Lumeva Botanics Natural baby skin and hair care

We need a look and feel for a line of baby care products. A lotion, Wash and baby oil. We already have an existing line of products and are now venturing into baby care. We want a natural look with "love, softness and a touch of earth and Africa'

Industry/Entity Type

Retail

Font styles to use
Script

Colors
fbed22
f78f20
9bcb3c

Requirements
Must have
• Natural elements
Should not have
• Red, Black abstract shapes

```html
<!DOCTYPE html>
<html lang="en">
<head>
<meta charset="utf-8">
<title>Lumeva Botanics – Baby Care Labels</title>
<link rel="stylesheet" href="https://fonts.googleapis.com/css2?family=Courgette&family=Open+Sans:wght@400;600;700&display=swap">
<style>
  :root {
    --bg: #e4eaec;
    --orange: #f26a2e;
    --orange-soft: #f78f20;
    --yellow: #fbed22;
    --green-light: #9bcb3c;
    --green: #1f9a48;
    --green-deep: #137a3a;
    --ink: #1d2a22;
    --white: #ffffff;
    --logo-ink: #6f7768;
  }
  * { box-sizing: border-box; margin: 0; padding: 0; }
  html, body { width: 1200px; height: 901px; overflow: hidden; }
  body {
    background: var(--bg);
    font-family: "Open Sans", Arial, sans-serif;
    position: relative;
  }
  .label {
    position: absolute;
    background: linear-gradient(180deg, var(--orange) 0%, var(--orange-soft) 22%, var(--yellow) 50%, var(--green-light) 74%, var(--green) 100%);
    text-align: center;
    overflow: hidden;
  }
  .label--oil { left: 163px; top: 312px; width: 197px; height: 446px; border-radius: 98px 98px 98px 98px / 100px 100px 110px 110px; }
  .label--lotion { left: 449px; top: 245px; width: 263px; height: 542px; border-radius: 131px 131px 131px 131px / 135px 135px 150px 150px; }
  .label--wash { left: 780px; top: 245px; width: 266px; height: 542px; border-radius: 133px 133px 133px 133px / 135px 135px 150px 150px; }

  .brand-box {
    position: absolute; left: 50%; transform: translateX(-50%);
    background: var(--white);
    display: flex; align-items: center; justify-content: center;
    color: var(--logo-ink); font-weight: 400; line-height: 1.2;
    letter-spacing: 0.06em; text-transform: uppercase;
  }
  .label--oil .brand-box { top: 89px; width: 74px; height: 74px; font-size: 8px; }
  .label--lotion .brand-box,
  .label--wash .brand-box { top: 75px; width: 92px; height: 94px; font-size: 10px; }

  .copy { position: absolute; left: 0; right: 0; }
  .label--oil .copy { top: 178px; }
  .label--lotion .copy, .label--wash .copy { top: 178px; }

  .kicker { color: var(--ink); font-weight: 400; }
  .label--oil .kicker { font-size: 16px; }
  .label--lotion .kicker, .label--wash .kicker { font-size: 20px; }

  .product {
    font-family: "Courgette", cursive;
    color: var(--green-deep);
    line-height: 1.05;
  }
  .label--oil .product { font-size: 28px; }
  .label--lotion .product, .label--wash .product { font-size: 33px; }

  .ingredients { color: var(--ink); font-weight: 700; line-height: 1.3; margin-top: 4px; }
  .label--oil .ingredients { font-size: 11.5px; }
  .label--lotion .ingredients, .label--wash .ingredients { font-size: 13.5px; }

  .mascot {
    position: absolute; left: 50%; transform: translateX(-50%);
    border-radius: 45% 45% 40% 40%;
  }
  .label--oil .mascot { top: 290px; width: 86px; height: 92px; background: radial-gradient(circle at 50% 40%, #e8941f 0%, #d9321e 70%); }
  .label--lotion .mascot { top: 312px; width: 122px; height: 118px; background: radial-gradient(circle at 50% 45%, #f4f4f4 0%, #8d8d8d 70%); }
  .label--wash .mascot { top: 318px; width: 106px; height: 112px; background: radial-gradient(circle at 50% 45%, #b9bac4 0%, #e9a3c4 85%); }

  .volume { position: absolute; left: 0; right: 0; color: var(--ink); font-weight: 700; line-height: 1.2; }
  .label--oil .volume { top: 388px; font-size: 13.5px; font-weight: 400; }
  .label--lotion .volume, .label--wash .volume { top: 466px; font-size: 17px; }

  .tagline { position: absolute; left: 0; top: 0; pointer-events: none; }
  .tagline text { fill: var(--white); font-family: "Open Sans", Arial, sans-serif; font-weight: 700; }
</style>
</head>
<body>

  <section class="label label--oil">
    <div class="brand-box">Lumeva<br>Botanics</div>
    <div class="copy">
      <p class="kicker">100% Natural</p>
      <h2 class="product">Baby Oil</h2>
      <p class="ingredients">Pure Shea Oil, &amp; Marula Oil<br>with Myrrh &amp; Frankinsence</p>
    </div>
    <div class="mascot" role="img" aria-label="Cartoon lion cub mascot"></div>
    <p class="volume">100ml/3.38oz</p>
    <svg class="tagline" width="197" height="446" viewBox="0 0 197 446">
      <path id="arc-oil" d="M 9 318 A 89.5 118 0 0 0 188 318" fill="none"/>
      <text font-size="13.5"><textPath href="#arc-oil" startOffset="50%" text-anchor="middle">Nurture, Moisturise, Protect</textPath></text>
    </svg>
  </section>

  <section class="label label--lotion">
    <div class="brand-box">Lumeva<br>Botanics</div>
    <div class="copy">
      <p class="kicker">Natural</p>
      <h2 class="product">Baby Lotion</h2>
      <p class="ingredients">All Natural Shea Butter<br>&amp; Honey baby lotion</p>
    </div>
    <div class="mascot" role="img" aria-label="Cartoon zebra foal mascot"></div>
    <p class="volume">250ml/8oz</p>
    <svg class="tagline" width="263" height="542" viewBox="0 0 263 542">
      <path id="arc-lotion" d="M 16 390 A 115 130 0 0 0 247 390" fill="none"/>
      <text font-size="18"><textPath href="#arc-lotion" startOffset="50%" text-anchor="middle">Moisturising and Soothing</textPath></text>
    </svg>
  </section>

  <section class="label label--wash">
    <div class="brand-box">Lumeva<br>Botanics</div>
    <div class="copy">
      <p class="kicker">Natural</p>
      <h2 class="product">Baby Wash</h2>
      <p class="ingredients">Shea Butter<br>&amp; Chamomile</p>
    </div>
    <div class="mascot" role="img" aria-label="Cartoon baby elephant mascot"></div>
    <p class="volume">250ml/8oz</p>
    <svg class="tagline" width="266" height="542" viewBox="0 0 266 542">
      <path id="arc-wash" d="M 18 390 A 115 130 0 0 0 248 390" fill="none"/>
      <text font-size="18"><textPath href="#arc-wash" startOffset="50%" text-anchor="middle">Bath and Body Wash</textPath></text>
    </svg>
  </section>

</body>
</html>
```